Real Estate Investment Company

Design Powerpoint slides are consistent with our logo, colors, and typeface. These Powerpoint slides will be used in all aspects of the business from live presentations to presentation decks available on a website or via email. Need to have different slide types created that allow for different types of slides such as cover pages, text heavy pages, image and chart heavy pages, multiple column pages, and mixed content pages.

Reason: to give additional time to get the design correct. I plan on making a selection in the next day or 2

Target Market(s)

Real Estate Investors

Industry/Entity Type

Investment

Other font styles liked:
• Consistent with logo

Requirements
Must have
• Our colors
• Our logo where possible
• Different slide designs of the same theme to allow for different types of slides such as cover pages, text heavy, picture heavy, and mixed content.
• Slides in both portrait and landscape orientation
Nice to have

```html
<!DOCTYPE html>
<html lang="en">
<head>
<meta charset="UTF-8">
<title>Our Services</title>
<link href="https://fonts.googleapis.com/css2?family=Roboto+Condensed:wght@400;700&display=swap" rel="stylesheet">
<style>
  :root {
    --navy: #1e2d6e;
    --ink: #333333;
    --white: #ffffff;
    --paper: #ffffff;
    --strip: #f4e6dc;
  }
  * { margin: 0; padding: 0; box-sizing: border-box; }
  html, body { width: 1200px; height: 900px; overflow: hidden; background: var(--paper); }
  body { font-family: "Roboto Condensed", Arial, sans-serif; color: var(--ink); }
  .slide { position: relative; width: 1200px; height: 900px; overflow: hidden; background: var(--paper); }

  .side-column {
    position: absolute; left: 0; top: 0; width: 293px; height: 900px;
    background: var(--strip);
    box-shadow: 4px 0 10px rgba(0,0,0,0.18);
    z-index: 2;
  }
  .brand {
    position: absolute; left: 0; top: 12px; width: 293px; height: 135px;
    background: var(--white);
    display: flex; align-items: center; justify-content: center; gap: 12px;
    padding: 0 16px;
  }
  .brand-mark { width: 22px; height: 22px; background: var(--navy); flex: none; }
  .brand-name {
    color: var(--navy); font-weight: 400; font-size: 21px; line-height: 1.2;
    text-transform: uppercase; letter-spacing: 0.5px;
  }
  .side-photo {
    position: absolute; left: 0; top: 147px; width: 293px; height: 753px;
    background: linear-gradient(180deg, #7a5a44 0%, #a07a58 35%, #d9a56a 55%, #8a5a3a 80%, #4a2a1a 100%);
  }

  .section-title {
    position: absolute; left: 905px; top: 0; width: 268px; height: 112px;
    background: var(--navy); color: var(--white);
    font-weight: 700; font-size: 45px;
    display: flex; align-items: center; justify-content: center;
  }

  .intro {
    position: absolute; left: 332px; top: 140px; width: 848px;
    font-size: 20.5px; line-height: 34.5px;
  }

  .service { position: absolute; top: 315px; width: 406px; }
  .service-1 { left: 332px; }
  .service-2 { left: 771px; width: 401px; }
  .service-photo {
    width: 100%; height: 305px; border: 4px solid var(--white);
    box-shadow: 0 0 7px rgba(0,0,0,0.45);
  }
  .photo-kitchen { background: linear-gradient(180deg, #c8c0a8 0%, #9a7048 50%, #6e4a2a 100%); }
  .photo-living { background: linear-gradient(180deg, #d8d2b8 0%, #c0a878 50%, #8a7a68 100%); }
  .service-title {
    margin-top: 36px; color: var(--navy); font-weight: 700; font-size: 30px; line-height: 36px;
  }
  .service-2 .service-title, .service-2 .service-text { margin-left: 12px; }
  .service-text { margin-top: 10px; font-size: 20.5px; line-height: 34.5px; width: 395px; }
</style>
</head>
<body>
<div class="slide">
  <aside class="side-column">
    <div class="brand">
      <span class="brand-mark"></span>
      <span class="brand-name">Ridgeline Management Corporation</span>
    </div>
    <div class="side-photo" role="img" aria-label="Blurred warm living room interior with bookshelf, lamp and orange cushions"></div>
  </aside>

  <h1 class="section-title">Our Servies</h1>

  <p class="intro">Lorem Ipsum is simply dummy text of the printing and typesetting industry. Lorem Ipsum has been the industry's standard dummy text ever since the 1500s, Lorem Ipsum is simply dummy text of the printing and typesetting industry. Lorem Ipsum has been the industry's standard dummy text ever since the 1500s,</p>

  <section class="service service-1">
    <div class="service-photo photo-kitchen" role="img" aria-label="Apartment kitchen with wooden cabinets, window and white refrigerator"></div>
    <h2 class="service-title">Service Title Here</h2>
    <p class="service-text">Lorem Ipsum is simply dummy text of the printing and typesetting industry. Lorem Ipsum has been the industry's standard dummy text ever since the 1500s</p>
  </section>

  <section class="service service-2">
    <div class="service-photo photo-living" role="img" aria-label="Furnished living room with sofa, armchair, fireplace and bright window"></div>
    <h2 class="service-title">Service Title Here</h2>
    <p class="service-text">Lorem Ipsum is simply dummy text of the printing and typesetting industry. Lorem Ipsum has been the industry's standard dummy text ever since the 1500s</p>
  </section>
</div>
</body>
</html>
```